Tallowfen Capital Group - letterhead

We need a corporate letterhead template (word) and slide show template (PowerPoint) designed for our investment business Tallowfen Capital Group.

Tallowfen Capital Group manages a group of investments in Australia and are after a letterhead template and PowerPoint template that is both creative and professional in design.

Information to be included on the letterhead (word) template is as follows:

Level 4, 318 Marlow Road
Kew VIC 3101

t. 03 5127 6618

Please feel free to ask any questions.

Investment

```html
<!DOCTYPE html>
<html lang="en">
<head>
<meta charset="utf-8">
<title>Tallowfen Capital Group – Letterhead and Cover</title>
<link href="https://fonts.googleapis.com/css2?family=Cinzel:wght@400&family=Montserrat:wght@400;700&display=swap" rel="stylesheet">
<style>
  :root {
    --backdrop: #eeeeee;
    --paper: #f7f7f7;
    --brand-blue: #1b6aa3;
    --cover-blue: #17659a;
    --cover-accent: #2cd3e3;
    --footer-grey: #555b62;
  }
  html, body {
    margin: 0;
    padding: 0;
    width: 1200px;
    height: 815px;
    overflow: hidden;
    background: var(--backdrop);
  }
  .canvas {
    position: relative;
    width: 1200px;
    height: 815px;
  }
  .sheet {
    position: absolute;
    top: 70px;
    width: 483px;
    height: 683px;
  }
  .letterhead {
    left: 80px;
    background: var(--paper);
  }
  .cover {
    left: 638px;
    background: var(--cover-blue);
  }
  .brand-name {
    font-family: "Cinzel", serif;
    font-weight: 400;
    margin: 0;
    white-space: nowrap;
  }
  .letterhead .brand-name {
    position: absolute;
    left: 50px;
    top: 62px;
    font-size: 15px;
    letter-spacing: 0.5px;
    color: var(--brand-blue);
  }
  .cover .brand-name {
    position: absolute;
    left: 0;
    right: 0;
    top: 322px;
    text-align: center;
    font-size: 29px;
    letter-spacing: 1px;
    color: var(--cover-accent);
  }
  .footer-details {
    position: absolute;
    left: 50px;
    top: 637px;
    margin: 0;
    font-family: "Montserrat", sans-serif;
    font-size: 6px;
    color: var(--footer-grey);
    white-space: nowrap;
  }
  .footer-details .label {
    font-weight: 700;
    color: var(--brand-blue);
  }
  .footer-rule {
    position: absolute;
    left: 50px;
    top: 655px;
    width: 380px;
    height: 2px;
    background: var(--brand-blue);
  }
</style>
</head>
<body>
  <main class="canvas">
    <section class="sheet letterhead" aria-label="Letterhead">
      <h1 class="brand-name">Tallowfen Capital Group</h1>
      <p class="footer-details">Level 4, 318 Marlow Road, Kew VIC 3101 · <span class="label">Phone:</span> 03 5127 6618</p>
      <div class="footer-rule"></div>
    </section>
    <section class="sheet cover" aria-label="Cover">
      <h2 class="brand-name">Tallowfen Capital Group</h2>
    </section>
  </main>
</body>
</html>
```